RevelHubQZ Business Cards

Front
Has logo with a design. Website address (www.revelhubqz.example)
Has slogan (discover nightlife)
Has phone number (5129873304)
Should be bold and stands out.

Back
Has details about what we offer.

Events
Search upcoming events
Submit events
Party Image Gallery
View and download HQ party images
Sign up as a contributing event photographer and get paid!
Tickets
Sell your event tickets online for free!
Direct pay
No ticket fee

Target Market(s)

These cards will be handed out in clubs and events to patrons.

Industry/Entity Type

Business

Contact Information for Business Card

Should match or mirror our website in some sort of way. Visit the website to get ideas.

Requirements
Must have
• Must be designed for a 3x3 inch card.

```html
<!DOCTYPE html>
<html lang="en">
<head>
<meta charset="utf-8">
<title>RevelHubQZ Business Cards</title>
<link href="https://fonts.googleapis.com/css2?family=Didact+Gothic&display=swap" rel="stylesheet">
<style>
  :root {
    --bg: #2b2b2d;
    --card-dark: #050505;
    --card-light: #ffffff;
    --blue: #2fa3dc;
    --pink: #e5399a;
    --ink: #2a2a2a;
    --muted: #8d8d8d;
  }
  * { box-sizing: border-box; margin: 0; padding: 0; }
  html, body { width: 1200px; height: 800px; overflow: hidden; }
  body {
    background: var(--bg);
    font-family: "Didact Gothic", "Century Gothic", sans-serif;
    position: relative;
  }
  .card {
    position: absolute;
    top: 190px;
    width: 420px;
    height: 420px;
    border-radius: 26px;
    overflow: hidden;
    box-shadow: 0 18px 40px rgba(0,0,0,.45);
  }
  .card--front { left: 150px; background: var(--card-dark); }
  .card--back  { left: 630px; background: var(--card-light); }

  .edge-band {
    position: absolute; left: 0; right: 0; bottom: 0; height: 16px;
    display: flex;
  }
  .edge-band__blue { flex: 0 0 42%; background: var(--blue); }
  .edge-band__pink { flex: 1; background: var(--pink); }

  /* Front */
  .brand {
    position: absolute; top: 62px; left: 0; right: 0;
    display: flex; flex-direction: column; align-items: center;
  }
  .brand__row { display: flex; align-items: center; gap: 12px; }
  .brand__dot { width: 22px; height: 22px; border-radius: 50%; background: var(--blue); }
  .brand__name { color: var(--blue); font-size: 38px; letter-spacing: .5px; }
  .brand__tagline {
    margin-top: 4px; color: var(--muted); font-size: 13px;
    letter-spacing: 6px; text-transform: lowercase;
  }
  .contact {
    position: absolute; top: 200px; right: 44px; text-align: right;
  }
  .contact__name { font-size: 27px; font-weight: bold; color: var(--blue); }
  .contact__name span { color: var(--pink); }
  .contact__role { color: #e8e8e8; font-size: 17px; margin-top: 2px; }
  .contact__phone { color: #ffffff; font-size: 22px; margin-top: 16px; letter-spacing: 1px; }
  .contact__web { color: var(--blue); font-size: 18px; margin-top: 6px; }

  /* Back */
  .offer { position: absolute; top: 44px; left: 56px; right: 36px; }
  .offer__title { font-size: 30px; color: var(--blue); text-align: center; margin-bottom: 18px; }
  .offer__title span { color: var(--pink); }
  .offer__list { list-style: none; }
  .offer__item {
    display: flex; align-items: flex-start; gap: 7px;
    font-size: 14.5px; color: var(--ink); line-height: 1.35; margin-bottom: 2px;
  }
  .offer__item--sub { padding-left: 20px; }
  .offer__bullet {
    flex: 0 0 9px; height: 9px; margin-top: 5px;
    border-radius: 50%; background: var(--blue);
  }
  .social {
    position: absolute; left: 70px; bottom: 54px; display: flex; gap: 10px;
  }
  .social__square { width: 26px; height: 26px; border-radius: 3px; background: var(--pink); }
</style>
</head>
<body>

<section class="card card--front" aria-label="Card front">
  <div class="brand">
    <div class="brand__row">
      <span class="brand__dot"></span>
      <span class="brand__name">RevelHubQZ</span>
    </div>
    <div class="brand__tagline">discover nightlife</div>
  </div>
  <div class="contact">
    <div class="contact__name">Dara <span>Velon</span></div>
    <div class="contact__role">Manager</div>
    <div class="contact__phone">+1 512-987-3304</div>
    <div class="contact__web">www.revelhubqz.example</div>
  </div>
  <div class="edge-band"><div class="edge-band__blue"></div><div class="edge-band__pink"></div></div>
</section>

<section class="card card--back" aria-label="Card back">
  <div class="offer">
    <h2 class="offer__title">what <span>we</span> offer</h2>
    <ul class="offer__list">
      <li class="offer__item"><span class="offer__bullet"></span>Events</li>
      <li class="offer__item offer__item--sub"><span class="offer__bullet"></span>Search upcoming events</li>
      <li class="offer__item offer__item--sub"><span class="offer__bullet"></span>Submit events</li>
      <li class="offer__item"><span class="offer__bullet"></span>Party Image Gallery</li>
      <li class="offer__item offer__item--sub"><span class="offer__bullet"></span>View and download HQ party images</li>
      <li class="offer__item offer__item--sub"><span class="offer__bullet"></span>Sign up as a contributing event photographer and get paid!</li>
      <li class="offer__item"><span class="offer__bullet"></span>Tickets</li>
      <li class="offer__item offer__item--sub"><span class="offer__bullet"></span>Sell your event tickets online for free!</li>
      <li class="offer__item offer__item--sub"><span class="offer__bullet"></span>Direct pay</li>
      <li class="offer__item offer__item--sub"><span class="offer__bullet"></span>No ticket fee</li>
    </ul>
  </div>
  <div class="social" aria-label="Social profiles">
    <span class="social__square"></span>
    <span class="social__square"></span>
    <span class="social__square"></span>
  </div>
  <div class="edge-band"><div class="edge-band__blue"></div><div class="edge-band__pink"></div></div>
</section>

</body>
</html>
```